Brochure Design Project

Please design a corporate brochure for my business "Corvin Asbestos & Safety"

Specs:-
- A4 flat size, three panel front, three panel back, roll-folded to DL
- Portrait orientation
- Full colour
Updates

Please don't forget to send in your designs. I believe the competition ends in a few hours. Thank you!

Target Market(s)

Business owners, commercial/industrial building owners, real estate property managers, strata managers

Industry/Entity Type

Business

Requirements
Must have
• - Professional / modern but serious as the content is important
- Cover page in particular must stand out so it will be noticeable if sitting on someone's desk
- Good use of whitespace and not too crowded
- Heading highlighted in warm/hot colour i.e. burnt orange, all other text in black
- Font Georgia 11pt
Nice to have
• - I have uploaded our letterhead source files too - please weave in the theme/look and feel of the letterhead into the brochure if possible.

```html
<!DOCTYPE html>
<html lang="en">
<head>
<meta charset="utf-8">
<title>Corvin Asbestos &amp; Safety – Asbestos Compliance</title>
<link rel="stylesheet" href="https://fonts.googleapis.com/css2?family=Fjalla+One&family=Gelasio:ital,wght@0,400;0,700;1,700&display=swap">
<style>
  :root{
    --hazard-yellow:#ebe32b;
    --ink:#1a1a1a;
    --white:#ffffff;
    --burnt-orange:#f4901e;
    --callout-orange:#f39a1f;
    --leaf-green:#7dc242;
    --navy:#2e2d52;
    --diagram-pink:#f2c6cf;
    --diagram-soft:#f7eef0;
  }
  *{margin:0;padding:0;box-sizing:border-box}
  html,body{width:1200px;height:846px;overflow:hidden;background:var(--white)}
  .brochure{position:relative;width:1200px;height:846px;overflow:hidden;font-family:"Gelasio",Georgia,serif;color:var(--ink)}

  /* hazard strip */
  .hazard-strip{position:absolute;left:0;top:0;width:1200px;height:57px;background:var(--hazard-yellow);display:flex;justify-content:space-around;align-items:center;padding:0 6px}
  .hazard-tag{display:flex;align-items:center;gap:6px}
  .hazard-tag svg{width:40px;height:34px}
  .hazard-label{font-family:"Fjalla One",Impact,sans-serif;font-size:14px;line-height:14px;text-align:center;color:#111;letter-spacing:-.2px}

  .panel{position:absolute;top:57px;height:758px}
  .panel-left{left:0;width:400px}
  .panel-mid{left:400px;width:401px}
  .panel-right{left:801px;width:399px}

  /* left panel */
  .edge-bar{position:absolute;left:0;top:46px;width:24px;height:677px;background:#000}
  .diagram{position:absolute;left:24px;top:6px;width:376px;height:322px;background:radial-gradient(circle at 70% 30%,var(--diagram-pink) 0 22%,transparent 23%),radial-gradient(ellipse at 35% 75%,var(--diagram-pink) 0 30%,var(--diagram-soft) 60%,var(--white) 80%)}
  .section-bar{position:absolute;left:0;top:330px;width:382px;height:52px;background:var(--burnt-orange);color:var(--white);font-family:"Fjalla One",Impact,sans-serif;font-size:25px;line-height:52px;padding-left:16px;letter-spacing:.2px;white-space:nowrap}
  .panel-left .copy{position:absolute;left:38px;top:392px;width:342px}

  .copy p{font-size:16.6px;line-height:25.7px}
  .copy p + p{margin-top:25.7px}
  .copy em{font-weight:700;font-style:italic}
  .copy strong{font-weight:700}

  /* heading tabs */
  .tab{position:absolute;left:0;top:0}
  .tab-title{position:absolute;font-family:"Fjalla One",Impact,sans-serif;color:var(--white);line-height:1}
  .panel-mid .tab-title{left:40px;top:10px}
  .tab-title .big{display:block;font-size:42px;letter-spacing:.3px}
  .tab-title .sub{display:block;font-size:24px;line-height:29px}
  .panel-right .tab-title{left:40px;top:10px}
  .panel-right .tab-title .big{font-size:40px;line-height:42px}

  .panel-mid .copy{position:absolute;left:20px;top:205px;width:364px}
  .panel-mid .copy p + p{margin-top:11px}
  .fine-callout{position:absolute;left:206px;top:658px;width:192px;text-align:center;font-weight:700;font-size:16px;line-height:18px;white-space:nowrap}
  .fine-callout .amount{display:block;color:var(--callout-orange);font-size:25px;line-height:29px;letter-spacing:-.3px}

  .panel-right .copy{position:absolute;left:20px;top:210px;width:344px}

  /* foot bands */
  .foot{position:absolute;left:0;top:815px;width:1200px;height:31px}
</style>
</head>
<body>
<div class="brochure">

  <header class="hazard-strip" aria-label="Danger asbestos warnings">
    <div class="hazard-tag"><svg viewBox="0 0 40 34"><path d="M20 2 L38 32 H2 Z" fill="none" stroke="#111" stroke-width="3" stroke-linejoin="round"/><rect x="18.5" y="11" width="3" height="12" fill="#111"/><rect x="18.5" y="25" width="3" height="3" fill="#111"/></svg><span class="hazard-label">DANGER<br>ASBESTOS</span></div>
    <div class="hazard-tag"><svg viewBox="0 0 40 34"><path d="M20 2 L38 32 H2 Z" fill="none" stroke="#111" stroke-width="3" stroke-linejoin="round"/><rect x="18.5" y="11" width="3" height="12" fill="#111"/><rect x="18.5" y="25" width="3" height="3" fill="#111"/></svg><span class="hazard-label">DANGER<br>ASBESTOS</span></div>
    <div class="hazard-tag"><svg viewBox="0 0 40 34"><path d="M20 2 L38 32 H2 Z" fill="none" stroke="#111" stroke-width="3" stroke-linejoin="round"/><rect x="18.5" y="11" width="3" height="12" fill="#111"/><rect x="18.5" y="25" width="3" height="3" fill="#111"/></svg><span class="hazard-label">DANGER<br>ASBESTOS</span></div>
    <div class="hazard-tag"><svg viewBox="0 0 40 34"><path d="M20 2 L38 32 H2 Z" fill="none" stroke="#111" stroke-width="3" stroke-linejoin="round"/><rect x="18.5" y="11" width="3" height="12" fill="#111"/><rect x="18.5" y="25" width="3" height="3" fill="#111"/></svg><span class="hazard-label">DANGER<br>ASBESTOS</span></div>
    <div class="hazard-tag"><svg viewBox="0 0 40 34"><path d="M20 2 L38 32 H2 Z" fill="none" stroke="#111" stroke-width="3" stroke-linejoin="round"/><rect x="18.5" y="11" width="3" height="12" fill="#111"/><rect x="18.5" y="25" width="3" height="3" fill="#111"/></svg><span class="hazard-label">DANGER<br>ASBESTOS</span></div>
    <div class="hazard-tag"><svg viewBox="0 0 40 34"><path d="M20 2 L38 32 H2 Z" fill="none" stroke="#111" stroke-width="3" stroke-linejoin="round"/><rect x="18.5" y="11" width="3" height="12" fill="#111"/><rect x="18.5" y="25" width="3" height="3" fill="#111"/></svg><span class="hazard-label">DANGER<br>ASBESTOS</span></div>
    <div class="hazard-tag"><svg viewBox="0 0 40 34"><path d="M20 2 L38 32 H2 Z" fill="none" stroke="#111" stroke-width="3" stroke-linejoin="round"/><rect x="18.5" y="11" width="3" height="12" fill="#111"/><rect x="18.5" y="25" width="3" height="3" fill="#111"/></svg><span class="hazard-label">DANGER<br>ASBESTOS</span></div>
    <div class="hazard-tag"><svg viewBox="0 0 40 34"><path d="M20 2 L38 32 H2 Z" fill="none" stroke="#111" stroke-width="3" stroke-linejoin="round"/><rect x="18.5" y="11" width="3" height="12" fill="#111"/><rect x="18.5" y="25" width="3" height="3" fill="#111"/></svg><span class="hazard-label">DANGER<br>ASBESTOS</span></div>
  </header>

  <section class="panel panel-left">
    <div class="edge-bar"></div>
    <div class="diagram" role="img" aria-label="Medical diagram of pleural mesothelioma showing asbestos fibres entering the lungs and a magnified view of diseased mesothelial cells"></div>
    <h2 class="section-bar">Why is Asbestos so dangerous?</h2>
    <div class="copy">
      <p>Asbestos is a hazardous substance that poses a risk to health by inhalation if the asbestos fibres become airborne. Exposure to these fibres is known to cause <em>mesothelioma, asbestosis and lung cancer.</em></p>
      <p>Australia had the highest per capita use of asbestos in the world in the 1950s and it is not surprising that it has the <em>world’s highest incidence of asbestos related cancer.</em> Asbestos has caused a significant death toll and much suffering in Australia, and the impact of <em>asbestos-related diseases is expected to peak in 2020.</em></p>
    </div>
  </section>

  <section class="panel panel-mid">
    <svg class="tab" width="401" height="186" viewBox="0 0 401 186"><polygon points="0,0 401,0 401,146 0,186" fill="var(--leaf-green)"/></svg>
    <h2 class="tab-title"><span class="big">Are you</span><span class="sub">compliant with current<br>Work Health and Safety (WHS)<br>legislation regarding<br>Asbestos?</span></h2>
    <div class="copy">
      <p>The Work Health and Safety (WHS) Act (2011) requires that <em>a person conducting a business or undertaking (PCBU) must ensure, as far as reasonably practicable, the health and safety of their workers</em><span style="color:var(--burnt-orange)">.</span></p>
      <p>Further, the Work Health and Safety (WHS) Regulation (2011) and its associated Code of Practice – How to Manage and Control Asbestos in the Workplace <em>requires the person with management or control of a workplace to ensure, so far as is reasonably practicable, that all asbestos at the workplace is identified.</em> This applies to all non-domestic buildings constructed prior to 31st December 2003 – commercial, retail, industrial, community, educational, healthcare,<br>accommodation and the<br>common property of<br>strata developments.</p>
    </div>
    <p class="fine-callout">Fines of<span class="amount">up to $30,000</span>apply for<br>non-compliance</p>
  </section>

  <section class="panel panel-right">
    <svg class="tab" width="399" height="186" viewBox="0 0 399 186"><polygon points="0,0 399,0 399,146 62,184 0,156" fill="var(--navy)"/></svg>
    <h2 class="tab-title"><span class="sub">How can</span><span class="big">you protect your</span><span class="sub">workers, contractors<br>and visitors from<br>exposure to Asbestos?</span></h2>
    <div class="copy">
      <p>You can protect your workers, contractors and visitors by exercising your Duty of Care and meeting the requirements of the current legislation to put in place an <strong>Asbestos Register</strong> and <strong>Management Plan</strong> for your building.</p>
      <p>The <strong>Asbestos Register</strong> is a document that lists all identified – or assumed – asbestos in a workplace.</p>
      <p>The person with management or control of a workplace must ensure an <strong>asbestos register</strong> is prepared and kept at the workplace and reviewed periodically.</p>
      <p>The <strong>Asbestos Management Plan</strong> helps the person with management or control of the workplace prevent exposure to airborne asbestos fibres at the workplace.</p>
    </div>
  </section>

  <svg class="foot" viewBox="0 0 1200 31" preserveAspectRatio="none" aria-hidden="true">
    <polygon points="0,0 243,0 222,31 0,31" fill="var(--navy)"/>
    <polygon points="258,0 400,0 400,31 237,31" fill="var(--leaf-green)"/>
    <polygon points="400,0 640,0 620,31 400,31" fill="var(--navy)"/>
    <polygon points="655,0 801,0 801,31 635,31" fill="var(--leaf-green)"/>
    <polygon points="801,0 1050,0 1030,31 801,31" fill="var(--navy)"/>
    <polygon points="1065,0 1200,0 1200,31 1045,31" fill="var(--leaf-green)"/>
  </svg>

</div>
</body>
</html>
```